依頼詳細
コーポレートカラーがオレンジなので、オレンジをベースにデザインをお願いしたいと思っております。
見やすさ、内容の伝わりやすさ、先進的なイメージを与えつつ、信頼できる雰囲気のチラシデザインだと嬉しいです。
イメージ画像や写真などは独自にご提案いただいて構いません。
よろしくお願い致します。
記載項目
素案のファイルを添付します
サイズ
A4
ページ数
両面
希望イメージ
シンプル 複雑
単色 カラフル
暗い 明るい
日常 高級
遊び心 厳粛
未来的 伝統的
女性的 男性的
希望する色
黄・オレンジ系
納品ファイル
• 高解像度JPG (.jpg)
• イラストレーター形式 (.ai)
• フォトショップ形式 (.psd)
• PNG形式 (.png)
補足説明

伝わりやすいデザインで、独自のキャッチコピー提案がありました。裏面も見やすい形でデザインしていただけてとてもよかったです。ありがとうございました。

この度はお忙しい中、ご提案いただきましてありがとうございました。
また機会がございましたら、ご提案いただけますと幸いです。

```html
<!DOCTYPE html>
<html lang="ja">
<head>
<meta charset="UTF-8">
<title>AI 業務自動化ソリューション</title>
<link rel="stylesheet" href="https://fonts.googleapis.com/css2?family=Noto+Sans+JP:wght@400;500;700;900&family=M+PLUS+1p:wght@500;800&family=Orbitron:wght@500;700&display=swap">
<style>
  :root{
    --orange:#f08a1c;
    --orange-light:#ffb347;
    --orange-pale:#fdebd3;
    --dark:#1b0f06;
    --dark-mid:#3a1d07;
    --ink:#2b2b2b;
    --grey:#6b6b6b;
    --white:#ffffff;
    --blue-grey:#7b8a99;
  }
  *{margin:0;padding:0;box-sizing:border-box}
  html,body{width:849px;height:1200px;overflow:hidden;background:#fff}
  body{font-family:"Noto Sans JP",sans-serif;color:var(--ink)}
  .flyer{position:relative;width:849px;height:1200px;overflow:hidden;background:var(--white)}

  .hero{position:absolute;left:0;top:0;width:849px;height:590px;
    background:radial-gradient(ellipse at 50% 35%,#a9550e 0%,#5a2a08 35%,var(--dark) 75%);}
  .hero-visual{position:absolute;inset:0;
    background:radial-gradient(circle at 20% 60%,rgba(255,160,50,.35),transparent 30%),
               radial-gradient(circle at 85% 25%,rgba(255,170,60,.3),transparent 30%),
               radial-gradient(circle at 50% 20%,rgba(255,200,110,.35),transparent 25%);}
  .brand{position:absolute;left:26px;top:20px;font-family:"Noto Sans JP",sans-serif;
    font-weight:700;font-size:22px;color:var(--white);letter-spacing:.02em}

  .title-ai{position:absolute;left:360px;top:38px;width:130px;height:88px;
    border:3px solid var(--orange-light);border-radius:4px;
    display:flex;align-items:center;justify-content:center;
    font-family:"Orbitron",sans-serif;font-weight:500;font-size:72px;color:var(--white);
    text-shadow:0 0 14px var(--orange-light);box-shadow:0 0 16px rgba(255,170,60,.6)}
  .title-main{position:absolute;left:0;width:849px;text-align:center;
    font-family:"M PLUS 1p",sans-serif;font-weight:800;color:#ffd9a0;
    text-shadow:0 0 10px var(--orange),0 0 22px var(--orange)}
  .title-1{top:128px;font-size:80px;letter-spacing:.08em}
  .title-band{position:absolute;left:212px;top:218px;width:425px;height:26px;
    background:linear-gradient(90deg,transparent,rgba(240,138,28,.85) 15%,rgba(240,138,28,.85) 85%,transparent);
    font-family:"Orbitron",sans-serif;font-size:15px;font-weight:500;color:var(--white);
    letter-spacing:.12em;text-align:center;line-height:26px}
  .title-2{top:246px;font-size:78px;letter-spacing:.06em}

  .lead{position:absolute;left:0;top:345px;width:849px;text-align:center;
    color:var(--white);font-size:16px;line-height:1.95;font-weight:500;padding-left:150px}

  .hero-edge{position:absolute;left:0;top:540px}

  .section-head{position:absolute;left:42px;top:600px;display:flex;align-items:center;gap:14px}
  .section-head .bar{width:6px;height:40px;background:var(--orange)}
  .section-head h2{font-size:32px;font-weight:700;color:var(--orange);letter-spacing:.04em}
  .section-head h2 .en{font-family:"Orbitron",sans-serif;font-weight:500;margin-right:10px}
  .subhead{position:absolute;left:44px;top:650px;font-size:17px;font-weight:700;color:var(--ink)}
  .subhead::after{content:"";display:block;width:470px;height:1px;background:#ccc;margin-top:8px}
  .points{position:absolute;left:44px;top:690px;list-style:none;font-size:15px;line-height:1.75;font-weight:500}
  .points li::before{content:"●";color:var(--ink);margin-right:6px;font-size:12px}

  .diagram{position:absolute;left:0;top:760px;width:849px;height:400px}
  .ai-core{position:absolute;left:58px;top:150px;font-family:"Orbitron",sans-serif;
    font-weight:500;font-size:60px;color:var(--blue-grey)}
  .feature{position:absolute;left:268px;width:540px;height:92px;display:flex;align-items:center}
  .feature .tag{width:120px;height:62px;border-radius:31px;background:var(--white);
    border:2px solid var(--orange);display:flex;flex-direction:column;align-items:center;justify-content:center;
    color:var(--orange);position:relative;z-index:1;box-shadow:0 2px 6px rgba(0,0,0,.12)}
  .feature .tag small{font-size:12px;font-weight:700}
  .feature .tag b{font-family:"Orbitron",sans-serif;font-size:24px;font-weight:700;line-height:1}
  .feature .body{margin-left:-30px;flex:1;height:92px;border-radius:46px;
    background:var(--orange-pale);padding:12px 24px 0 48px}
  .feature h3{font-size:17px;font-weight:700;color:var(--orange);margin-bottom:4px}
  .feature p{font-size:11.5px;line-height:1.55;color:var(--ink)}
  .f1{top:20px}.f2{top:134px}.f3{top:248px}

  .footer-strip{position:absolute;left:0;bottom:0;width:849px;height:22px;
    background:linear-gradient(90deg,var(--orange),var(--orange-light))}
</style>
</head>
<body>
<div class="flyer">
  <header class="hero">
    <div class="hero-visual" role="img" aria-label="オレンジに光るネットワーク回路と光の粒のイメージ"></div>
    <div class="brand">Lumivox</div>
    <div class="title-ai">AI</div>
    <h1>
      <span class="title-main title-1">業務自動化</span>
      <span class="title-band">AI BUSINESS AUTOMATION SOLUTION</span>
      <span class="title-main title-2">ソリューション</span>
    </h1>
    <p class="lead">
      AIによって業務を効率化・自動化し、<br>
      お客さまのパフォーマンス最大化を支援します。<br>
      最適なデバイスの選定、ソフト・ハードの設置、テスト、<br>
      PDCAサイクルまで、<br>
      トータルに導入をサポートします。
    </p>
  </header>

  <svg class="hero-edge" width="849" height="60" viewBox="0 0 849 60">
    <polygon points="0,20 849,0 849,60 0,60" fill="#fff"/>
  </svg>

  <section class="analysis">
    <div class="section-head">
      <span class="bar"></span>
      <h2><span class="en">AI</span>動画解析</h2>
    </div>
    <p class="subhead">ヒト・モノ・コトの特徴をリアルタイムに検出</p>
    <ul class="points">
      <li>人物の属性情報の取得、製造・物流現場での不良品の検出、危険エリアへの侵入検知</li>
      <li>人の目に頼っていた作業の自動化や、業務効率化、安全対策の支援を可能にします</li>
    </ul>

    <div class="diagram">
      <svg width="849" height="400" viewBox="0 0 849 400" style="position:absolute;left:0;top:0">
        <path d="M20 20 A190 190 0 0 1 20 360" fill="none" stroke="#f4b36a" stroke-width="3" transform="translate(0,0)"/>
        <path d="M-100 20 A210 180 0 0 1 -100 380" fill="none" stroke="#f08a1c" stroke-width="2" transform="translate(0,0)"/>
        <path d="M30 45 Q230 190 30 345" fill="none" stroke="#f08a1c" stroke-width="6" stroke-linecap="round"/>
        <line x1="180" y1="66" x2="268" y2="66" stroke="#f08a1c" stroke-width="2"/>
        <line x1="220" y1="180" x2="268" y2="180" stroke="#f08a1c" stroke-width="2"/>
        <line x1="180" y1="294" x2="268" y2="294" stroke="#f08a1c" stroke-width="2"/>
      </svg>
      <div class="ai-core">AI</div>

      <div class="feature f1">
        <div class="tag"><small>特徴</small><b>01</b></div>
        <div class="body">
          <h3>業務効率化支援</h3>
          <p>お客さまの業務の現状をしっかり把握し、<br>最適な改善策をご提案、プロセス全体での改善を図ります。</p>
        </div>
      </div>
      <div class="feature f2">
        <div class="tag"><small>特徴</small><b>02</b></div>
        <div class="body">
          <h3>高精度の認識率</h3>
          <p>AI画像認識ノウハウと効果的な学習を<br>組み合わせることで、高精度の認識を実現します。</p>
        </div>
      </div>
      <div class="feature f3">
        <div class="tag"><small>特徴</small><b>03</b></div>
        <div class="body">
          <h3>解析＋アルファ</h3>
          <p>解析するだけでなく、データの可視化・分析、<br>デバイスへの通知等、柔軟に対応いたします。</p>
        </div>
      </div>
    </div>
  </section>

  <div class="footer-strip"></div>
</div>
</body>
</html>
```